automatic Real Estate Sales Brochure

Print-out of 3 to 8 pages automatically on a color inkjet printer. Page size A4
All details for my Real Estate Sales Design Project are in attached file.
Here some points:
We have abound 100 real estate objects for sale (houses, flats and pieces of land).
For each item, our system creates automatically a sales documentation, which we print out and hand to the potential buyers after they've visited the object or send it by mail upon request in form of a pdf.
This document should be of 3 to maximum 8 pages.
It should be of a modern design and invite the client to read it.
The information should be clear and quick to find.
If the global look could somehow relate to the look of our web site www.velorancasa.ch, that would be nice.
The company data is there for legal reasons, but it is the agent's phone and mail that the clients should use for contact.
The photos should be of big size (2 by page?) without being distorted nor cut.
Optionally, to save ink and pages, maybe only the first 3-4 photos full size and the rest smaller?

Target Market(s)

will be printed or sent as PDF "on the fly", meaning no pre-printing at a print shop!

Industry/Entity Type

Real Estate

Font styles to use
Sans Serif

Requirements
Must have
• see details in attached file
Should not have
• no edge-to-edge printing
• no double-page printing (A3)

```html
<!DOCTYPE html>
<html lang="fr">
<head>
<meta charset="utf-8">
<title>Brochure de vente – 4.5 pièces Genève</title>
<link href="https://fonts.googleapis.com/css2?family=Roboto:wght@300;400;500;700&display=swap" rel="stylesheet">
<style>
  :root{
    --ink:#2d2d2d;
    --muted:#6b6e72;
    --band:#e3e5e8;
    --cell:#e7e9eb;
    --head:#aeb2b7;
    --accent:#d2232a;
    --frame:#111;
  }
  *{box-sizing:border-box;margin:0;padding:0}
  html,body{width:1200px;height:1113px;overflow:hidden;background:#fff}
  body{position:relative;font-family:"Roboto",Arial,sans-serif;color:var(--ink)}
  .page{position:absolute;width:391px;height:552px;border:2px solid var(--frame);background:#fff;overflow:hidden}
  .p1{left:0;top:0}.p2{left:404px;top:0}.p3{left:809px;top:0}
  .p4{left:0;top:561px}.p5{left:404px;top:561px}

  .topband{position:absolute;left:0;right:0;top:0;height:62px;background:var(--band)}
  .agent{position:absolute;right:28px;top:20px;text-align:right;font-size:7.6px;line-height:11px;color:#444}
  .agent b{font-weight:500;letter-spacing:.2px}
  .brandbox{position:absolute;left:0;top:0;width:158px;height:126px;background:#fff;padding:24px 0 0 27px;z-index:2}
  .brand-name{font-size:17px;font-weight:700;color:var(--accent);line-height:18px;letter-spacing:.2px}
  .brand-tag{font-size:3.6px;color:var(--muted);letter-spacing:.2px;margin-top:2px}
  .company{margin-top:9px;font-size:7.4px;line-height:9.4px;color:#333}
  .company b{font-weight:700;letter-spacing:.2px}
  .company .gap{height:5px}

  .photo{position:absolute;left:0;right:0;top:62px}
  .garden{height:292px;background:linear-gradient(180deg,#7fb3e6 0%,#b9d3c8 22%,#5f8f3a 45%,#3d6a22 75%,#2f5418 100%)}
  .living{height:290px;background:linear-gradient(180deg,#d7c2a3 0%,#efe4d2 35%,#dfcdb3 58%,#c98a45 70%,#a86428 100%)}
  .bedroom{height:242px;background:linear-gradient(90deg,#f2d58e 0%,#e9c278 35%,#3a2f29 45%,#241d19 100%)}
  .hall{height:292px;background:linear-gradient(90deg,#e8e0cf 0%,#f0efe9 35%,#f4f3ef 70%,#c0a07a 100%)}
  .room{height:292px;background:linear-gradient(180deg,#f0efea 0%,#e9e7e1 50%,#c99a5e 72%,#a56f34 100%)}
  .thumb{position:absolute;top:357px;height:144px;width:193px}
  .thumb.a{left:0}.thumb.b{left:196px}
  .open-plan{background:linear-gradient(180deg,#eceae4 0%,#e2d7c5 50%,#b58148 100%)}
  .corridor{background:linear-gradient(90deg,#e3ddcf 0%,#d4c3a5 50%,#eeece6 100%)}
  .bath{background:linear-gradient(180deg,#eef0f1 0%,#dfe3e6 60%,#c8cdd2 100%)}
  .footband{position:absolute;left:0;right:0;top:502px;bottom:0;background:var(--band)}

  .title{position:absolute;left:0;right:0;top:376px;text-align:center}
  .title h1{font-size:17.5px;font-weight:500;letter-spacing:.1px;color:#333}
  .title p{font-size:17px;font-weight:300;color:#333;margin-top:3px}

  table.facts{position:absolute;left:27px;top:428px;width:336px;border-collapse:collapse;font-size:6.8px}
  table.facts td{background:var(--cell);height:24px;border:2px solid #fff;padding:0 7px}
  table.facts td.v{text-align:right;color:#888;font-weight:300}
  table.facts td.k{color:#333}

  .amenities{position:absolute;left:27px;top:378px;width:336px}
  .amenities h2{background:var(--head);color:#fff;font-weight:400;font-size:12px;text-align:center;height:25px;line-height:25px}
  .amenities table{width:100%;border-collapse:collapse;font-size:6.8px}
  .amenities td{background:var(--cell);height:24px;border:2px solid #fff;padding:0 7px;line-height:8px}
  .amenities td.v{text-align:right;color:#888;font-weight:300}

  .description{position:absolute;left:28px;right:26px;top:329px;font-size:6.4px;line-height:8.6px;color:#555;font-weight:300;text-align:justify}
  .description h3{font-size:6.6px;font-weight:400;color:#333}
  .description p{margin-bottom:6px}

  .note{position:absolute;left:888px;top:832px;font-size:28px;font-weight:300;color:#111}
  .pointer{position:absolute;left:0;top:0}
</style>
</head>
<body>

<!-- Page 1 -->
<section class="page p1">
  <div class="topband"></div>
  <div class="agent"><b>VOTRE COURTIER NADIA MOREL</b><br>077 555 01 23 - morel@velorancasa.ch</div>
  <div class="brandbox">
    <div class="brand-name">Veloranca</div>
    <div class="brand-tag">SPÉCIALISTE ROMAND DE VENTE IMMOBILIÈRE</div>
    <div class="company"><b>VELORANCA SÀRL</b><br>1806 Mont-Brel<div class="gap"></div>www.velorancasa.ch<br>Tel. 021 555 40 12</div>
  </div>
  <div class="photo garden" role="img" aria-label="Jardin arboré de la résidence avec arbres et buissons"></div>
  <div class="title">
    <h1>LUMINEUX 4.5 DE 100m² IDÉALEMENT SITUÉ</h1>
    <p>1200 Genève</p>
  </div>
  <table class="facts">
    <tr><td class="k">Type de bien</td><td class="v">Appartement</td><td class="k">Prix</td><td class="v">CHF 910 000.-</td></tr>
    <tr><td class="k">Surface habitable m²</td><td class="v">100 m²</td><td class="k">Année de</td><td class="v">1994</td></tr>
    <tr><td class="k">Nombre de pièces</td><td class="v">4,5</td><td class="k">Etat</td><td class="v">Bon état</td></tr>
    <tr><td class="k">Surface parcelle m2</td><td class="v">1000 m²</td><td class="k">Libre dès le</td><td class="v">01.01.2018</td></tr>
  </table>
</section>

<!-- Page 2 -->
<section class="page p2">
  <div class="topband"></div>
  <div class="agent"><b>VOTRE COURTIER NADIA MOREL</b><br>077 555 01 23 - morel@velorancasa.ch</div>
  <div class="brandbox">
    <div class="brand-name">Veloranca</div>
    <div class="brand-tag">SPÉCIALISTE ROMAND DE VENTE IMMOBILIÈRE</div>
    <div class="company"><b>VELORANCA SÀRL</b><br>1806 Mont-Brel<div class="gap"></div>www.velorancasa.ch<br>Tel. 021 555 40 12</div>
  </div>
  <div class="photo living" role="img" aria-label="Séjour lumineux avec parquet et portes-fenêtres sur le balcon"></div>
  <div class="amenities">
    <h2>Commodités</h2>
    <table>
      <tr><td>Etage</td><td class="v">1 er étage</td><td>Chauffage</td><td class="v">mazout / au sol</td></tr>
      <tr><td>Vue</td><td class="v">dégagée sur le parc</td><td>Cave</td><td class="v">oui</td></tr>
      <tr><td>Commerces</td><td class="v">proximité immédiate</td><td>Garage</td><td class="v">2 places de parc<br>intérieures</td></tr>
      <tr><td>Ecoles</td><td class="v">Collège des Tilleuls</td><td>Balcon</td><td class="v">oui</td></tr>
      <tr><td>Transports publics</td><td class="v">à 5 minutes à pied</td><td>Ascenseur</td><td class="v">oui</td></tr>
    </table>
  </div>
</section>

<!-- Page 3 -->
<section class="page p3">
  <div class="topband"></div>
  <div class="agent"><b>VOTRE COURTIER NADIA MOREL</b><br>077 555 01 23 - morel@velorancasa.ch</div>
  <div class="brandbox">
    <div class="brand-name">Veloranca</div>
    <div class="brand-tag">SPÉCIALISTE ROMAND DE VENTE IMMOBILIÈRE</div>
    <div class="company"><b>VELORANCA SÀRL</b><br>1806 Mont-Brel<div class="gap"></div>www.velorancasa.ch<br>Tel. 021 555 40 12</div>
  </div>
  <div class="photo bedroom" role="img" aria-label="Chambre avec grande armoire encastrée à portes coulissantes"></div>
  <div class="description">
    <h3>Description:</h3>
    <p>Le visiteur pourra trouver un bel appartement dans une zone respectueuse de l'environnement et dynamique avec une vue sur le centre de la ville et les marchés communaux. Les bénéfices de beaux volumes et de pièces de vie très lumineuses. C'est le cas pour quelques années, donc il y a un bien pour un couple ou une famille.</p>
    <p>Cet appartement pourrait aussi convenir comme investissement pour un client souhaitant le louer. L'est en bon et d'entretien et se réjouit d'accueillir ses nouveaux propriétaires!</p>
    <p>Si elle distribue ainsi:<br>Ils se confient à l'armoire encastrée desserte de part et d'autre la fête et la partie nuit. La spacieuse pièce de vie est composée d'une cuisine, et c'est entièrement équipée et aménagée s'ouvrant sur le séjour. Le profit d'une exposition optimale. Là vous pouvez trouver une belle vue dégagée sur un environnement verdoyant. La fête de la nuit offre trois belles chambres, salle de bains avec baignoire, lavabo, wc ainsi que wc visiteurs.</p>
    <p>Deux emplacements de parc intérieur en une s'outeur de ce appartement!</p>
    <p>Contactez-nous pour plus d'informations et obtenir plus d'informations!</p>
    <h3>Situation :</h3>
    <p>Cet appartement à l'avantage de se situer proche de toutes les commodités, à 3 minutes du Collège des Tilleuls, à 1 minute de l'arrêt de bus et à 3 minutes des axes autoroutiers. Vous rejoindrez le centre-villas en 7 minutes. Des aiuts que vous saurez apprécier.</p>
  </div>
</section>

<!-- Page 4 -->
<section class="page p4">
  <div class="topband"></div>
  <div class="agent"><b>VOTRE COURTIER NADIA MOREL</b><br>077 555 01 23 - morel@velorancasa.ch</div>
  <div class="brandbox">
    <div class="brand-name">Veloranca</div>
    <div class="brand-tag">SPÉCIALISTE ROMAND DE VENTE IMMOBILIÈRE</div>
    <div class="company"><b>VELORANCA SÀRL</b><br>1806 Mont-Brel<div class="gap"></div>www.velorancasa.ch<br>Tel. 021 555 40 12</div>
  </div>
  <div class="photo hall" role="img" aria-label="Cuisine équipée et hall d'entrée avec armoires murales"></div>
  <div class="thumb a open-plan" role="img" aria-label="Espace de vie ouvert avec cuisine et parquet"></div>
  <div class="thumb b corridor" role="img" aria-label="Couloir menant aux chambres"></div>
  <div class="footband"></div>
</section>

<!-- Page 5 -->
<section class="page p5">
  <div class="topband"></div>
  <div class="agent"><b>VOTRE COURTIER NADIA MOREL</b><br>077 555 01 23 - morel@velorancasa.ch</div>
  <div class="brandbox">
    <div class="brand-name">Veloranca</div>
    <div class="brand-tag">SPÉCIALISTE ROMAND DE VENTE IMMOBILIÈRE</div>
    <div class="company"><b>VELORANCA SÀRL</b><br>1806 Mont-Brel<div class="gap"></div>www.velorancasa.ch<br>Tel. 021 555 40 12</div>
  </div>
  <div class="photo room" role="img" aria-label="Chambre vide avec grande fenêtre et parquet"></div>
  <div class="thumb a bath" role="img" aria-label="Salle de bains avec lavabo, wc et baignoire"></div>
  <div class="footband"></div>
</section>

<div class="note">White space</div>
<svg class="pointer" width="1200" height="1113" viewBox="0 0 1200 1113" aria-hidden="true">
  <line x1="953" y1="879" x2="740" y2="991" stroke="#111" stroke-width="1.2"/>
</svg>

</body>
</html>
```